まず、縦を想定しており、画像をメインにした構成を想定しております。

上半分は覚悟を決めた中年以上の料理にが仁王立ちしているようなイメージの写真で「店を売るという選択」or「店をゆずる決断」というキャプション

下半分はやる気に満ち溢れた若者が覚悟を持って仁王立ちしているようなイメージ
「店を買う」or「店(歴史)を引きつぐ覚悟」というキャプション

そして、下の方に計算式添付の資料にあるような表を挿入。
売却した方は結局、いくら得したのか。買った方はいくら得したのかがわかるように。あとは、「査定無料」「神奈川エリアに特化した唯一のエージェントです」を記載お願いします。最後にヴェルコハーバーズという社名と連絡先を記載。

全体的なイメージではノルヴェクや外国の広告のようにシンプルだけどもどこかデザイン性を感じるように。また、信頼性も大事なので全体的にシックだけども目を引くように。
VELKO HARBORS
ヴェルコハーバーズ
0120-471-362
www.velko-harbors-jp.example
A4
片面
青系、茶系、グレー系
• 高解像度JPG (.jpg)
• イラストレーター形式 (.ai)
キャプションの修正
【メインキャプション】大事なお店、最も高く売却いたします。
【売手側キャプション】 お店を売るという選択
【買手側キャプション】お店を買うという選択

また、各キャプションを大きめに表示をお願いします。

全体的にまとまっており、柔軟に対応頂いたため。

ありがとうござました!!

```html
<!DOCTYPE html>
<html lang="ja">
<head>
<meta charset="utf-8">
<title>ヴェルコハーバーズ 店舗売買</title>
<link rel="stylesheet" href="https://fonts.googleapis.com/css2?family=Noto+Sans+JP:wght@400;700;900&family=Noto+Serif+JP:wght@600&display=swap">
<style>
:root{
  --brown:#3a2a1f;
  --brown-line:#8a7563;
  --orange:#ee8a12;
  --cream:#f4ece1;
  --paper:#ffffff;
  --photo-a:#ece9e4;
  --photo-b:#b9ada0;
}
*{margin:0;padding:0;box-sizing:border-box}
html,body{width:848px;height:1200px;overflow:hidden;background:var(--paper)}
body{font-family:"Noto Sans JP",sans-serif;color:var(--cream)}
.poster{position:relative;width:848px;height:1200px;overflow:hidden;background:var(--paper)}
.hero-photo{position:absolute;left:0;top:0;width:848px;height:922px;
  background:linear-gradient(100deg,var(--photo-a) 0%,#d8d3cc 45%,var(--photo-b) 100%)}
.hero-frame{position:absolute;left:14px;top:14px;width:820px;height:894px;border:1px solid rgba(255,255,255,.7)}
.headline{position:absolute;writing-mode:vertical-rl;font-weight:900;color:var(--orange);
  font-size:76px;line-height:1;letter-spacing:4px;text-shadow:0 0 6px rgba(255,255,255,.6)}
.headline--sell{left:428px;top:112px}
.headline--start{left:222px;top:128px}
.info-band{position:absolute;left:0;top:922px;width:848px;height:278px;background:var(--brown)}
.sim{position:absolute;top:18px;width:300px}
.sim--open{left:52px}
.sim--close{left:440px;width:230px}
.sim-title{font-size:11px;text-align:center;border-bottom:1px solid var(--brown-line);padding-bottom:3px;margin-bottom:3px}
.sim table{width:100%;border-collapse:collapse;font-size:10px}
.sim td,.sim th{padding:3px 4px;border-bottom:1px solid var(--brown-line);font-weight:400;text-align:right}
.sim th:first-child,.sim td:first-child{text-align:left}
.sim tr.total td{border-bottom:none;font-weight:700}
.result{position:absolute;top:22px;width:124px;height:124px;border-radius:50%;border:1px solid var(--cream);
  display:flex;flex-direction:column;align-items:center;justify-content:center;text-align:center}
.result--open{left:290px}
.result--close{left:690px}
.result-amount{font-size:17px;font-weight:700;color:var(--cream)}
.result-note{font-size:11px;margin-top:4px}
.footer{position:absolute;left:0;bottom:0;width:848px;height:62px;display:flex;align-items:center;padding:0 26px;gap:20px}
.brand{display:flex;align-items:center;gap:8px;font-weight:700;font-size:14px;color:var(--cream)}
.brand-mark{width:22px;height:22px;background:var(--orange)}
.brand-sub{font-size:9px;font-weight:400;display:block}
.company{font-family:"Noto Serif JP",serif;font-size:20px;text-align:center;line-height:1.1}
.company small{display:block;font-family:"Noto Sans JP",sans-serif;font-size:10px}
.contact{margin-left:auto;text-align:right}
.tagline{font-size:12px;margin-bottom:4px}
.contact-row{display:flex;align-items:center;gap:4px;justify-content:flex-end}
.free{background:var(--cream);color:var(--brown);font-size:13px;font-weight:700;padding:1px 3px}
.phone{display:flex;align-items:center;gap:4px;font-size:26px;font-weight:700;margin-left:6px}
</style>
</head>
<body>
<main class="poster">
  <div class="hero-photo" role="img" aria-label="写真：左にメモを持つ笑顔の若い男性、右にフライパンで調理する料理人"></div>
  <div class="hero-frame"></div>
  <h1 class="headline headline--sell">お店を売りたい人から</h1>
  <p class="headline headline--start">始めたい人へ</p>

  <section class="info-band">
    <div class="sim sim--open" style="width:225px">
      <p class="sim-title">開店コストシミュレーション</p>
      <table>
        <tr><th></th><th>通常出店</th><th>当社サービス</th></tr>
        <tr><td>内装前備品費</td><td>13,000,000円</td><td>0円</td></tr>
        <tr><td>造作売買代金</td><td>0円</td><td>3,500,000円</td></tr>
        <tr class="total"><td>計</td><td>13,000,000円</td><td>3,500,000円</td></tr>
      </table>
    </div>
    <div class="result result--open">
      <span class="result-amount">9,500,000円</span>
      <span class="result-note">のコストダウン</span>
    </div>

    <div class="sim sim--close">
      <p class="sim-title">閉店コストシミュレーション</p>
      <table>
        <tr><th></th><th>通常閉店</th><th>当社サービス</th></tr>
        <tr><td>解約前予告家賃</td><td>1,000,000円</td><td>0円</td></tr>
        <tr><td>内装解体費</td><td>2,000,000円</td><td>0円</td></tr>
        <tr><td>造作売買代金</td><td>0円</td><td>2,000,000円</td></tr>
        <tr class="total"><td>計</td><td>△3,000,000円</td><td>2,000,000円</td></tr>
      </table>
    </div>
    <div class="result result--close">
      <span class="result-amount">3,000,000円</span>
      <span class="result-note">のメリット</span>
    </div>

    <footer class="footer">
      <div class="brand"><span class="brand-mark"></span><span>VELKO HARBORS<span class="brand-sub">ヴェルコハーバーズ</span></span></div>
      <div class="company">VELKO HARBORS<small>www.velko-harbors-jp.example</small></div>
      <div class="contact">
        <p class="tagline">神奈川エリアに特化した唯一のエージェントです</p>
        <div class="contact-row">
          <span class="free">査</span><span class="free">定</span><span class="free">無</span><span class="free">料</span>
          <span class="phone">
            <svg width="24" height="24" viewBox="0 0 24 24" aria-hidden="true"><path d="M6 3l4 4-2 3c1 2 3 4 6 6l3-2 4 4-3 3C10 20 4 14 3 6z" fill="var(--cream)"/></svg>
            0120-471-362
          </span>
        </div>
      </div>
    </footer>
  </section>
</main>
</body>
</html>
```